Graphic to show easy steps to find financial clarity

Howdy-I need a graphic that describe my Coin Compass Method.The attached is a concept, but please use your own creativity to show how you would display this:- There are 5 steps the process (and then we repeat/recalculate)- And three bullets that drive home the results of the processI've also attached my logo. Please use the colors in my logo and maybe add a soft green as needed.The reader should be able to briefly scan this document and understand that this is an easy/simple process that tells them how to manage their cash.Thanks!-Ned

Target Market(s)

wealthy women, whether single or married

Requirements
Must have
• Please use the colors in my logo and a soft green if needed
Should not have
• This should be a very easy to read graphic that communicates how simple/easy this is to do.

```html
<!DOCTYPE html>
<html lang="en">
<head>
<meta charset="utf-8">
<title>Coin Compass Method</title>
<link rel="stylesheet" href="https://fonts.googleapis.com/css2?family=Montserrat:wght@500;600;700&display=swap">
<style>
  :root {
    --backdrop: #dedede;
    --sheet: #ffffff;
    --brand-blue: #1d4f8b;
    --brand-navy: #163d6e;
    --ink-grey: #6b6b6b;
    --ink-dark: #333333;
    --icon-grey: #7a7a7a;
    --fill-soft: #c9d6e6;
  }
  html, body {
    margin: 0;
    padding: 0;
    width: 899px;
    height: 1200px;
    overflow: hidden;
    background: var(--backdrop);
  }
  .canvas {
    position: relative;
    width: 899px;
    height: 1200px;
  }
  .sheet {
    position: absolute;
    left: 0;
    top: 0;
    width: 899px;
    height: 1200px;
  }
  .sheet-bg { fill: var(--sheet); }
  .brand-name {
    font-family: "Montserrat", sans-serif;
    font-weight: 600;
    fill: var(--brand-navy);
  }
  .brand-mark { fill: var(--brand-blue); }
  .title-bar { fill: var(--brand-blue); }
  .title-text {
    font-family: "Montserrat", sans-serif;
    font-weight: 600;
    font-size: 27px;
    fill: #ffffff;
    letter-spacing: 0.3px;
  }
  .flow-line {
    fill: none;
    stroke: var(--brand-blue);
    stroke-width: 1.3;
    stroke-dasharray: 2 2;
  }
  .flow-arrow {
    fill: none;
    stroke: var(--brand-blue);
    stroke-width: 1.3;
  }
  .flow-start { fill: #ffffff; stroke: var(--brand-blue); stroke-width: 1.5; }
  .flow-end { fill: var(--brand-navy); }
  .step-number {
    font-family: "Montserrat", sans-serif;
    font-weight: 700;
    font-size: 92px;
    fill: var(--brand-blue);
  }
  .step-kicker {
    font-family: "Montserrat", sans-serif;
    font-weight: 600;
    font-size: 8.5px;
    fill: var(--ink-grey);
  }
  .step-label {
    font-family: "Montserrat", sans-serif;
    font-weight: 600;
    font-size: 10.5px;
    fill: var(--ink-grey);
  }
  .icon-line {
    fill: none;
    stroke: var(--icon-grey);
    stroke-width: 1.5;
    stroke-linejoin: round;
    stroke-linecap: round;
  }
  .icon-text {
    font-family: "Montserrat", sans-serif;
    font-weight: 600;
    font-size: 12px;
    fill: var(--icon-grey);
  }
  .result-tick {
    fill: none;
    stroke: var(--ink-dark);
    stroke-width: 1.1;
  }
  .result-text {
    font-family: "Montserrat", sans-serif;
    font-weight: 600;
    font-size: 9.8px;
    fill: var(--ink-dark);
  }
  .coins-art { fill: var(--fill-soft); }
</style>
</head>
<body>
<div class="canvas">
  <svg class="sheet" viewBox="0 0 850 1134" width="899" height="1200" xmlns="http://www.w3.org/2000/svg">
    <rect class="sheet-bg" x="170" y="207" width="503" height="750"/>

    <g class="brand">
      <rect class="brand-mark" x="306" y="286" width="40" height="40"/>
      <text class="brand-name" x="357" y="307" font-size="22">KESTREL BAY</text>
      <text class="brand-name" x="358" y="324" font-size="11.5">WEALTH MANAGEMENT</text>
    </g>

    <rect class="title-bar" x="209" y="364" width="425" height="63" rx="8"/>
    <text class="title-text" x="421" y="406" text-anchor="middle">COIN COMPASS METHOD</text>

    <line class="flow-line" x1="420" y1="440" x2="420" y2="490"/>
    <path class="flow-end" d="M414 487 L426 487 L420 497 Z"/>

    <circle class="flow-start" cx="208" cy="607" r="6"/>
    <path class="flow-line" d="M214 607 H620 Q630 607 630 617 V735 Q630 745 620 745 H214 Q204 745 204 755 V876 Q204 886 214 886 H512"/>
    <path class="flow-arrow" d="M329 602 L335 607 L329 612"/>
    <path class="flow-arrow" d="M473 602 L479 607 L473 612"/>
    <path class="flow-arrow" d="M494 740 L488 745 L494 750"/>
    <path class="flow-arrow" d="M352 740 L346 745 L352 750"/>
    <path class="flow-arrow" d="M262 881 L268 886 L262 891"/>
    <circle class="flow-end" cx="518" cy="886" r="6"/>

    <text class="step-number" x="221" y="596">1</text>
    <g class="step-icon">
      <rect class="icon-line" x="262" y="540" width="46" height="14" rx="2"/>
      <rect class="icon-line" x="271" y="550" width="28" height="42"/>
      <text class="icon-text" x="285" y="576" text-anchor="middle">$</text>
    </g>
    <text class="step-kicker" x="267" y="623" text-anchor="middle">KNOW YOUR</text>
    <text class="step-label" x="267" y="637" text-anchor="middle">ANNUAL SPENDING</text>

    <text class="step-number" x="363" y="596">2</text>
    <g class="step-icon">
      <rect class="icon-line" x="414" y="555" width="46" height="12"/>
      <rect class="icon-line" x="418" y="567" width="38" height="25"/>
      <line class="icon-line" x1="437" y1="555" x2="437" y2="592"/>
      <path class="icon-line" d="M437 555 C428 540 416 546 426 554 M437 555 C446 540 458 546 448 554"/>
    </g>
    <text class="step-kicker" x="414" y="623" text-anchor="middle">PROJECT</text>
    <text class="step-label" x="414" y="637" text-anchor="middle">SPECIAL EXPENSES</text>

    <text class="step-number" x="504" y="596">3</text>
    <g class="step-icon">
      <rect class="icon-line" x="557" y="540" width="42" height="52" rx="3"/>
      <rect class="icon-line" x="563" y="547" width="30" height="10"/>
      <path class="icon-line" d="M564 568 H572 M568 564 V572 M582 568 H591 M565 578 L571 584 M571 578 L565 584 M582 581 H591"/>
      <circle cx="586.5" cy="577.5" r="1" fill="#7a7a7a"/>
      <circle cx="586.5" cy="584.5" r="1" fill="#7a7a7a"/>
    </g>
    <text class="step-kicker" x="561" y="623" text-anchor="middle">ADD UP YOUR</text>
    <text class="step-label" x="561" y="637" text-anchor="middle">5 YEARS CASH NEEDS</text>

    <text class="step-number" x="213" y="734">6</text>
    <g class="step-icon">
      <rect class="icon-line" x="272" y="700" width="54" height="31" rx="3"/>
      <rect class="icon-line" x="283" y="686" width="32" height="14"/>
      <rect class="icon-line" x="292" y="676" width="14" height="10"/>
      <path class="icon-line" d="M282 709 H316 M282 716 H316 M290 724 H308"/>
    </g>
    <text class="step-kicker" x="269" y="761" text-anchor="middle">RECALCULATE</text>
    <text class="step-label" x="269" y="775" text-anchor="middle">MONTHLY</text>

    <text class="step-number" x="368" y="734">5</text>
    <g class="step-icon">
      <rect class="icon-line" x="422" y="684" width="42" height="24" transform="rotate(12 443 696)"/>
      <rect class="icon-line" x="432" y="706" width="42" height="24" transform="rotate(-6 453 718)"/>
      <text class="icon-text" x="439" y="703">$</text>
      <text class="icon-text" x="449" y="724">€</text>
    </g>
    <text class="step-kicker" x="422" y="761" text-anchor="middle">INVEST IN</text>
    <text class="step-label" x="422" y="775" text-anchor="middle">THE REST</text>

    <text class="step-number" x="496" y="734">4</text>
    <g class="step-icon">
      <circle class="icon-line" cx="589" cy="687" r="10"/>
      <text class="icon-text" x="589" y="692" text-anchor="middle">$</text>
      <path class="icon-line" d="M566 716 C566 701 583 697 595 700 C606 702 612 709 612 716 C612 724 606 728 602 730 V737 H595 V732 H580 V737 H573 V729 C569 727 566 722 566 716 Z"/>
      <path class="icon-line" d="M612 712 C616 712 618 709 617 706"/>
    </g>
    <text class="step-kicker" x="560" y="761" text-anchor="middle">SET THEM ASIDE</text>
    <text class="step-label" x="560" y="775" text-anchor="middle">IN SAVINGS</text>

    <g class="result-icon">
      <circle class="icon-line" cx="277" cy="825" r="28"/>
      <circle class="icon-line" cx="277" cy="825" r="17"/>
      <circle class="icon-line" cx="277" cy="825" r="6"/>
      <path class="icon-line" d="M234 825 H277 M234 825 L240 819 M234 825 L240 831 M241 825 L247 819 M241 825 L247 831"/>
      <path class="icon-line" d="M264 857 L261 869 M277 859 V871 M290 857 L293 869"/>
    </g>
    <g class="results">
      <path class="result-tick" d="M315 800 L318 803.5 L322 797"/>
      <text class="result-text" x="327" y="804">Know  your life style will be</text>
      <text class="result-text" x="327" y="818">unaffected by the markets for at</text>
      <text class="result-text" x="327" y="832">least 5 years</text>
      <path class="result-tick" d="M315 842 L318 845.5 L322 839"/>
      <text class="result-text" x="327" y="846">Spend intentionally and with joy</text>
      <path class="result-tick" d="M315 856 L318 859.5 L322 853"/>
      <text class="result-text" x="327" y="860">Create a solid base for lifetime</text>
      <text class="result-text" x="327" y="874">Cash Flow Projections</text>
    </g>

    <rect class="coins-art" x="528" y="790" width="104" height="98" rx="6" role="img" aria-label="Stacks of coins in front of a dollar banknote"/>
  </svg>
</div>
</body>
</html>
```